Wealth Education Business Needs Sharp Business Card Design

We need a business card design for a recently launched investor education business called Harbor Crest.

The final design should promote security, empowerment, self improvement and financial gain. The card will ideally promote the stature of the business.

For more information and colours please visit harborcrest.com.au

Target Market(s)

Corporate executives and high net worth individuals

Industry/Entity Type

Education

Contact Information for Business Card

Name
Position
Contact Address
Phone
Mobile
Email
Website

```html
<!DOCTYPE html>
<html lang="en">
<head>
<meta charset="utf-8">
<title>Harbor Crest — Business Card</title>
<link rel="stylesheet" href="https://fonts.googleapis.com/css2?family=Lato:wght@400;700&display=swap">
<style>
  :root {
    --backdrop: #e8e6e2;
    --navy: #1f2b3d;
    --paper: #ffffff;
    --teal: #14979b;
    --ink: #3a3a3c;
    --ink-soft: #4a4a4d;
    --band-grey: #5d5e63;
    --white: #ffffff;
  }
  * { margin: 0; padding: 0; box-sizing: border-box; }
  html, body {
    width: 1200px; height: 960px; overflow: hidden;
    background: var(--backdrop);
    font-family: "Lato", Arial, sans-serif;
  }
  .canvas { position: relative; width: 1200px; height: 960px; }

  .card {
    position: absolute; left: 270px; width: 645px; height: 368px;
    box-shadow: 0 4px 12px rgba(0,0,0,0.18);
    overflow: hidden;
  }
  .card--front { top: 83px; background: var(--navy); }
  .card--back { top: 507px; background: var(--paper); }

  .wordmark {
    position: absolute; left: 0; right: 0;
    font-weight: 400; text-transform: uppercase;
    letter-spacing: 0.16em; text-align: center; white-space: nowrap;
  }
  .card--front .wordmark { top: 62px; font-size: 42px; color: var(--white); }
  .card--back .wordmark {
    top: 72px; left: 55px; right: auto; text-align: left;
    font-size: 30px; color: var(--ink);
  }

  .front-url {
    position: absolute; left: 0; right: 0; top: 306px;
    text-align: center; font-size: 15px; color: var(--white);
  }
  .front-url .domain { color: var(--teal); }

  .person {
    position: absolute; right: 55px; top: 170px; text-align: right;
  }
  .person-name { font-size: 18px; font-weight: 700; color: var(--teal); line-height: 1.2; }
  .person-title { font-size: 14px; color: var(--ink-soft); line-height: 1.3; }

  .divider {
    position: absolute; left: 55px; right: 55px; top: 225px;
    height: 1.5px; background: var(--teal);
  }

  .contact-list {
    position: absolute; left: 55px; top: 249px; list-style: none;
  }
  .contact-list li {
    display: flex; align-items: center; height: 20.5px;
    font-size: 14.5px; color: var(--ink-soft);
  }
  .contact-list svg { width: 17px; height: 17px; margin-right: 12px; flex: none; }

  .address {
    position: absolute; right: 55px; top: 293px; text-align: right;
    font-size: 14.5px; line-height: 1.4; color: var(--ink-soft);
    font-style: normal;
  }

  .footer-band { position: absolute; left: 0; bottom: 0; width: 645px; height: 16px; }
</style>
</head>
<body>
<main class="canvas">

  <section class="card card--front" aria-label="Card front">
    <div class="wordmark">Harbor Crest</div>
    <p class="front-url">www.<span class="domain">harborcrest.com</span>.au</p>
  </section>

  <section class="card card--back" aria-label="Card back">
    <div class="wordmark">Harbor Crest</div>

    <div class="person">
      <p class="person-name">Daniel Whitford</p>
      <p class="person-title">Founder &amp; CEO</p>
    </div>

    <div class="divider"></div>

    <ul class="contact-list">
      <li>
        <svg viewBox="0 0 20 20" aria-hidden="true"><path fill="#14979b" d="M2 7c0-2 3-4 8-4s8 2 8 4v1h-4V6.5C12.8 6 11.5 6 10 6s-2.8 0-4 .5V8H2zM5 9h10l2 7H3z"/><circle cx="10" cy="12.5" r="2" fill="#fff"/></svg>
        1300.482.716
      </li>
      <li>
        <svg viewBox="0 0 20 20" aria-hidden="true"><rect x="5" y="1.5" width="10" height="17" rx="1.5" fill="none" stroke="#14979b" stroke-width="1.8"/><circle cx="10" cy="15.5" r="1" fill="#14979b"/></svg>
        0000.000.000
      </li>
      <li>
        <svg viewBox="0 0 20 20" aria-hidden="true"><rect x="1.5" y="4" width="17" height="12" fill="#14979b"/><path d="M1.5 4.5l8.5 6.5 8.5-6.5M1.5 15.5l6-5M18.5 15.5l-6-5" fill="none" stroke="#fff" stroke-width="1.3"/></svg>
        support@harborcrest.com.au
      </li>
      <li>
        <svg viewBox="0 0 20 20" aria-hidden="true"><g fill="none" stroke="#14979b" stroke-width="1.6"><circle cx="10" cy="10" r="8"/><ellipse cx="10" cy="10" rx="3.5" ry="8"/><path d="M2 10h16M3.5 5.5h13M3.5 14.5h13"/></g></svg>
        www.harborcrest.com.au
      </li>
    </ul>

    <address class="address">
      Level 4, 76 Quayside Lane<br>
      Portside VIC 3010
    </address>

    <svg class="footer-band" viewBox="0 0 645 16" preserveAspectRatio="none" aria-hidden="true">
      <polygon points="0,2 182,2 168,16 0,16" fill="#14979b"/>
      <polygon points="188,0 645,0 645,16 174,16" fill="#5d5e63"/>
    </svg>
  </section>

</main>
</body>
</html>
```